logo & Business Card Design

BrightHaven Termite & Pest Control, I need a great logo, take my ideas and run with them!
I will use this in marketing and website so needs to be eye catching but professional

Target Market(s)

Resedintial & Business

Industry/Entity Type

Marketing

Contact Information for Business Card

Need front side with pertinent info & Logo; back side will have a 25% off initial services Coupon!

Font styles to use
Sans Serif

Colors
ec1f27
1b1b1b

Requirements
Must have
• Professional logo and style
Nice to have
• Raised lettering, black, red, white colors maybe? I'm flexible, but those colors go good on any background, vehicle, uniform, etc...
Should not have
• Cheesy

```html
<!DOCTYPE html>
<html lang="en">
<head>
<meta charset="utf-8">
<title>BrightHaven Termite &amp; Pest Control – Business Card</title>
<link rel="stylesheet" href="https://fonts.googleapis.com/css2?family=Oswald:wght@600&family=Source+Sans+3:wght@400;600;700&display=swap">
<style>
  :root {
    --red: #ec1f27;
    --ink: #1b1b1b;
    --white: #ffffff;
    --grey: #8c8c8c;
    --backdrop: #cbbd9f;
  }
  html, body {
    margin: 0;
    padding: 0;
    width: 1200px;
    height: 1200px;
    overflow: hidden;
    background: var(--backdrop);
    font-family: "Source Sans 3", Arial, sans-serif;
  }
  .stage {
    position: relative;
    width: 1200px;
    height: 1200px;
  }
  .card {
    position: absolute;
    left: 236px;
    width: 730px;
    height: 436px;
    border-radius: 26px;
    background: var(--white);
    overflow: hidden;
    box-shadow: 0 6px 14px rgba(0,0,0,0.28);
  }
  .card--front { top: 140px; }
  .card--back { top: 658px; }
  .card__band {
    position: absolute;
    inset: 0;
    width: 100%;
    height: 100%;
  }
  .brand {
    position: absolute;
    top: 46px;
    left: 0;
    right: 0;
    display: flex;
    flex-direction: column;
    align-items: center;
  }
  .brand__row {
    display: flex;
    align-items: center;
    gap: 18px;
  }
  .brand__dot {
    width: 128px;
    height: 128px;
    border-radius: 50%;
    background: var(--ink);
    flex: none;
  }
  .brand__name {
    color: var(--ink);
    font-weight: 600;
    line-height: 1;
    padding-top: 18px;
  }
  .brand__name-main {
    display: block;
    font-size: 60px;
    letter-spacing: -0.5px;
  }
  .brand__name-sub {
    display: block;
    font-size: 27px;
    margin-top: 6px;
  }
  .brand__tagline {
    margin-top: 6px;
    font-size: 16px;
    color: var(--ink);
    font-weight: 400;
  }
  .person {
    position: absolute;
    left: 40px;
    top: 316px;
    width: 260px;
    text-align: center;
  }
  .person__name {
    color: var(--red);
    font-size: 36px;
    line-height: 1;
    font-weight: 400;
  }
  .person__title {
    color: var(--white);
    font-size: 21px;
    margin-top: 4px;
  }
  .contact {
    position: absolute;
    left: 362px;
    top: 306px;
    margin: 0;
    color: var(--white);
    font-size: 18px;
    line-height: 24px;
    display: grid;
    grid-template-columns: 34px auto;
  }
  .contact dt { font-weight: 600; margin: 0; }
  .contact dd { margin: 0; }
  .contact .accent { color: var(--red); font-weight: 600; }
  .offer {
    position: absolute;
    left: 0;
    right: 0;
    top: 280px;
    text-align: center;
    color: var(--white);
  }
  .offer__headline {
    font-family: "Oswald", Arial, sans-serif;
    font-weight: 600;
    font-size: 98px;
    line-height: 1;
  }
  .offer__detail {
    margin-top: 4px;
    font-size: 23px;
    letter-spacing: 7px;
    font-weight: 400;
  }
</style>
</head>
<body>
<main class="stage">

  <section class="card card--front" aria-label="Business card front">
    <svg class="card__band" viewBox="0 0 730 436" preserveAspectRatio="none" aria-hidden="true">
      <path d="M0 286 Q365 214 730 298 L730 436 L0 436 Z" fill="var(--grey)"/>
      <path d="M0 302 Q365 224 730 314 L730 436 L0 436 Z" fill="var(--ink)"/>
    </svg>
    <div class="brand">
      <div class="brand__row">
        <span class="brand__dot"></span>
        <div class="brand__name">
          <span class="brand__name-main">BrightHaven</span>
          <span class="brand__name-sub">Termite &amp; Pest Control</span>
        </div>
      </div>
      <div class="brand__tagline">"Trusted care for every home and business"</div>
    </div>
    <div class="person">
      <div class="person__name">Daniel Porter</div>
      <div class="person__title">President</div>
    </div>
    <dl class="contact">
      <dt>p:</dt><dd>555-014-2290</dd>
      <dt>e:</dt><dd>dan@<span class="accent">brighthavenpest.com</span></dd>
      <dt>w:</dt><dd>www.<span class="accent">brighthavenpestcontrol</span>.com</dd>
    </dl>
  </section>

  <section class="card card--back" aria-label="Business card back, coupon">
    <svg class="card__band" viewBox="0 0 730 436" preserveAspectRatio="none" aria-hidden="true">
      <path d="M0 290 Q365 206 730 302 L730 436 L0 436 Z" fill="var(--ink)"/>
      <path d="M0 302 Q365 218 730 317 L730 436 L0 436 Z" fill="var(--red)"/>
    </svg>
    <div class="brand">
      <div class="brand__row">
        <span class="brand__dot"></span>
        <div class="brand__name">
          <span class="brand__name-main">BrightHaven</span>
          <span class="brand__name-sub">Termite &amp; Pest Control</span>
        </div>
      </div>
      <div class="brand__tagline">"Trusted care for every home and business"</div>
    </div>
    <div class="offer">
      <div class="offer__headline">25% OFF</div>
      <div class="offer__detail">INITIAL SERVICES</div>
    </div>
  </section>

</main>
</body>
</html>
```